Tidewell Recovery Business Card Design

Professional and clean design. The design colors should flow with the logo. Two-sided card with the website on the back which is:

www.TidewellRecovery.example.

"Specializing in Water Damage Restoration"

On the front I need the name, email, phone, and logo.

Name: Dorian Vashti
Email: Dorian@TidewellRecovery.example
Phone: 555-318-2046 for now

I only have the Preview and Thumbnail right now but should have the source files uploaded within a day or two.

Target Market(s)

Flood victims, home owners with water damage from busted pipes etc...

Industry/Entity Type

Business

Contact Information for Business Card

Name: Dorian Vashti

Font styles to use
Serif
Sans Serif

```html
<!DOCTYPE html>
<html lang="en">
<head>
<meta charset="utf-8">
<title>Tidewell Recovery – Business Card</title>
<link rel="stylesheet" href="https://fonts.googleapis.com/css2?family=Open+Sans:wght@400;600&display=swap">
<style>
  :root {
    --page-bg: #e9ebee;
    --card-top: #fbfbfb;
    --card-bottom: #f1f2f3;
    --brand-blue: #1f7fcf;
    --band-blue: #2597d9;
    --logo-blue: #3aa3dd;
    --text-dark: #2b2b2b;
    --icon-blue: #1f6fb5;
    --white: #ffffff;
  }
  * { margin: 0; padding: 0; box-sizing: border-box; }
  html, body {
    width: 1200px;
    height: 900px;
    overflow: hidden;
    background: var(--page-bg);
    font-family: "Open Sans", Arial, sans-serif;
  }
  .business-card {
    position: absolute;
    left: 150px;
    top: 172px;
    width: 900px;
    height: 557px;
    background: linear-gradient(180deg, var(--card-top), var(--card-bottom));
    box-shadow: 0 6px 24px rgba(0, 0, 0, 0.12);
    overflow: hidden;
  }
  .holder-name {
    position: absolute;
    left: 63px;
    top: 46px;
    font-size: 33px;
    font-weight: 600;
    color: var(--brand-blue);
    letter-spacing: 0.2px;
  }
  .brand {
    position: absolute;
    left: 455px;
    top: 95px;
    width: 400px;
    text-align: center;
  }
  .brand-dot {
    display: block;
    width: 92px;
    height: 92px;
    margin: 0 auto 44px;
    border-radius: 50%;
    background: var(--logo-blue);
  }
  .brand-name {
    font-size: 31px;
    font-weight: 600;
    color: var(--brand-blue);
    letter-spacing: 2px;
    text-transform: uppercase;
    white-space: nowrap;
  }
  .contact-list {
    position: absolute;
    left: 63px;
    top: 366px;
    list-style: none;
  }
  .contact-item {
    display: flex;
    align-items: center;
    height: 33.5px;
    font-size: 22px;
    color: var(--text-dark);
  }
  .contact-icon {
    width: 16px;
    height: 16px;
    margin-right: 16px;
    flex: none;
  }
  .tagline-band {
    position: absolute;
    left: 0;
    bottom: 0;
    width: 100%;
    height: 68px;
    background: var(--band-blue);
    display: flex;
    align-items: center;
    justify-content: center;
    color: var(--white);
    font-size: 24px;
  }
</style>
</head>
<body>
  <section class="business-card">
    <h1 class="holder-name">Dorian Vashti</h1>

    <div class="brand">
      <span class="brand-dot"></span>
      <p class="brand-name">Tidewell Recovery</p>
    </div>

    <ul class="contact-list">
      <li class="contact-item">
        <svg class="contact-icon" viewBox="0 0 16 16" aria-hidden="true">
          <rect x="4" y="1" width="8" height="14" rx="1.5" fill="none" stroke="var(--icon-blue)" stroke-width="1.6"/>
          <circle cx="8" cy="12.3" r="0.9" fill="var(--icon-blue)"/>
        </svg>
        <span>555-318-2046</span>
      </li>
      <li class="contact-item">
        <svg class="contact-icon" viewBox="0 0 16 16" aria-hidden="true">
          <rect x="1" y="3" width="14" height="10" rx="1" fill="var(--icon-blue)"/>
          <path d="M1.5 3.8 L8 9 L14.5 3.8" fill="none" stroke="var(--white)" stroke-width="1.3"/>
        </svg>
        <span>Dorian@TidewellRecovery.example</span>
      </li>
      <li class="contact-item">
        <svg class="contact-icon" viewBox="0 0 16 16" aria-hidden="true">
          <g fill="none" stroke="var(--icon-blue)" stroke-width="1.7" stroke-linecap="round">
            <path d="M7 9 L9.5 6.5"/>
            <path d="M6.2 6.8 L4.3 8.7 a2.3 2.3 0 0 0 3.2 3.2 L9.4 10"/>
            <path d="M9.8 9.2 L11.7 7.3 a2.3 2.3 0 0 0 -3.2 -3.2 L6.6 6"/>
          </g>
        </svg>
        <span>www.TidewellRecovery.example</span>
      </li>
    </ul>

    <footer class="tagline-band">Specializing in Water Damage Restoration</footer>
  </section>
</body>
</html>
```